Stonegate Towing Business Card

Towing
Accident towing
Mechanical breakdown
Insurance, salvage and recovery
4wd off road towing
Light & Heavy towing
7354 2618
24 hour business 7 days

Logo can be whole size on front

Industry/Entity Type

Towing/ transport

Contact Information for Business Card

The above

```html
<!DOCTYPE html>
<html lang="en">
<head>
<meta charset="utf-8">
<title>Stonegate Towing Business Card</title>
<link href="https://fonts.googleapis.com/css2?family=Poppins:wght@500;600;700&display=swap" rel="stylesheet">
<style>
  :root {
    --backdrop: #c4c4c4;
    --brand-red: #d42027;
    --deep-red: #b01b21;
    --ink: #000000;
    --paper: #ffffff;
  }
  * { box-sizing: border-box; margin: 0; padding: 0; }
  html, body { width: 1093px; height: 1200px; overflow: hidden; }
  body {
    background: var(--backdrop);
    font-family: "Poppins", sans-serif;
    position: relative;
  }
  .card {
    position: absolute;
    left: 264px;
    width: 580px;
    height: 356px;
    border-radius: 30px;
    overflow: hidden;
  }
  .card-front { top: 226px; background: var(--brand-red); }
  .card-back { top: 622px; background: var(--ink); display: flex; align-items: center; justify-content: center; }

  .front-art { position: absolute; inset: 0; width: 100%; height: 100%; }

  .faint-name {
    position: absolute;
    left: 300px;
    top: 62px;
    width: 270px;
    text-align: center;
    font-weight: 700;
    font-size: 34px;
    line-height: 1.05;
    color: var(--deep-red);
    opacity: 0.55;
  }

  .service-list {
    position: absolute;
    left: 26px;
    top: 30px;
    list-style: none;
  }
  .service-list li {
    display: flex;
    align-items: center;
    height: 33px;
    font-weight: 600;
    font-size: 18px;
    letter-spacing: 0.1px;
    color: var(--paper);
    text-transform: uppercase;
  }
  .bullet {
    width: 16px; height: 16px;
    margin-right: 9px;
    flex: none;
  }

  .contact-row {
    position: absolute;
    left: 35px;
    right: 30px;
    top: 302px;
    height: 40px;
    display: flex;
    align-items: center;
  }
  .icon-badge {
    width: 38px; height: 38px;
    border-radius: 50%;
    background: var(--brand-red);
    flex: none;
    display: flex; align-items: center; justify-content: center;
  }
  .phone-number {
    margin-left: 12px;
    font-weight: 700;
    font-size: 35px;
    letter-spacing: -0.5px;
    color: var(--ink);
  }
  .hours {
    margin-left: auto;
    margin-right: 9px;
    font-weight: 500;
    font-size: 16px;
    color: var(--ink);
  }

  .brand-name {
    font-weight: 700;
    font-size: 46px;
    color: var(--brand-red);
    letter-spacing: 0.5px;
  }
</style>
</head>
<body>

<section class="card card-front">
  <svg class="front-art" viewBox="0 0 580 356" aria-hidden="true">
    <path d="M0 318 C60 270 120 250 200 252 C280 254 360 278 450 282 C520 285 545 245 580 190 L580 356 L0 356 Z" fill="var(--paper)"/>
    <path d="M0 318 C60 270 120 250 200 252 C280 254 360 278 450 282 C520 285 545 245 580 190" fill="none" stroke="var(--ink)" stroke-width="4"/>
    <path d="M330 258 C370 272 410 276 450 270 C410 274 370 270 330 258 Z" fill="none" stroke="var(--paper)" stroke-width="3" stroke-linecap="round"/>
  </svg>

  <div class="faint-name">Stonegate<br>Towing</div>

  <ul class="service-list">
    <li><svg class="bullet" viewBox="0 0 16 16"><rect x="3" y="3" width="10" height="10" transform="rotate(45 8 8)" fill="var(--paper)"/><rect x="5.5" y="5.5" width="5" height="5" transform="rotate(45 8 8)" fill="var(--brand-red)"/></svg>Towing</li>
    <li><svg class="bullet" viewBox="0 0 16 16"><rect x="3" y="3" width="10" height="10" transform="rotate(45 8 8)" fill="var(--paper)"/><rect x="5.5" y="5.5" width="5" height="5" transform="rotate(45 8 8)" fill="var(--brand-red)"/></svg>Accident towing</li>
    <li><svg class="bullet" viewBox="0 0 16 16"><rect x="3" y="3" width="10" height="10" transform="rotate(45 8 8)" fill="var(--paper)"/><rect x="5.5" y="5.5" width="5" height="5" transform="rotate(45 8 8)" fill="var(--brand-red)"/></svg>Mechanical breakdown</li>
    <li><svg class="bullet" viewBox="0 0 16 16"><rect x="3" y="3" width="10" height="10" transform="rotate(45 8 8)" fill="var(--paper)"/><rect x="5.5" y="5.5" width="5" height="5" transform="rotate(45 8 8)" fill="var(--brand-red)"/></svg>Insurance, salvage and recovery</li>
    <li><svg class="bullet" viewBox="0 0 16 16"><rect x="3" y="3" width="10" height="10" transform="rotate(45 8 8)" fill="var(--paper)"/><rect x="5.5" y="5.5" width="5" height="5" transform="rotate(45 8 8)" fill="var(--brand-red)"/></svg>4wd off road towing</li>
    <li><svg class="bullet" viewBox="0 0 16 16"><rect x="3" y="3" width="10" height="10" transform="rotate(45 8 8)" fill="var(--paper)"/><rect x="5.5" y="5.5" width="5" height="5" transform="rotate(45 8 8)" fill="var(--brand-red)"/></svg>Light &amp; heavy towing</li>
  </ul>

  <div class="contact-row">
    <span class="icon-badge">
      <svg width="20" height="20" viewBox="0 0 24 24" aria-hidden="true"><path d="M6.6 10.8a15.1 15.1 0 0 0 6.6 6.6l2.2-2.2a1 1 0 0 1 1-.25 11.4 11.4 0 0 0 3.6.57 1 1 0 0 1 1 1V20a1 1 0 0 1-1 1A17 17 0 0 1 3 4a1 1 0 0 1 1-1h3.5a1 1 0 0 1 1 1c0 1.25.2 2.45.57 3.57a1 1 0 0 1-.25 1z" fill="none" stroke="var(--paper)" stroke-width="1.6"/></svg>
    </span>
    <span class="phone-number">7354 2618</span>
    <span class="hours">24 hour business 7 days</span>
    <span class="icon-badge">
      <svg width="30" height="30" viewBox="0 0 30 30" aria-hidden="true"><circle cx="15" cy="15" r="11" fill="none" stroke="var(--paper)" stroke-width="1.6"/><text x="15" y="18" text-anchor="middle" font-family="Poppins, sans-serif" font-size="8" font-weight="600" fill="var(--paper)">24/7</text></svg>
    </span>
  </div>
</section>

<section class="card card-back">
  <span class="brand-name">Stonegate Towing</span>
</section>

</body>
</html>
```